Trifold Brochure

I am looking for someone to design a marketing brochure for my construction company, We specialise in residential construction contracts which are either high end, high specification luxury homes or in volume housebuilding, i.e projects with multiple houses of apartments being built.
The format of the brochure should be A5 when folded in a trifold format
Please utilise the logo (attached), the company website (www.holvane-builds.co.uk). Please also feel free to insert any copy or images you think will be suitable.
Please also follow the guidelines below:
1. Keep it simple: Don't overload your brochure with too much text or too many images. Stick to the most important information and use bullet points or short paragraphs to make it easy for people to scan and understand.
2. Use high-quality images: Use high-resolution images that are relevant to your message and showcase your product or service in a positive light.
3. Include a call to action: Make sure your brochure includes a clear call to action, such as "Contact us today to learn more" or "Visit our website to see our full product line."
4. Use a clean, professional layout: Use a clean, uncluttered layout that is easy to read and looks professional.
5. Make it easy to read: Use a font that is easy to read and not too small.

```html
<!DOCTYPE html>
<html lang="en">
<head>
<meta charset="utf-8">
<title>Holvane Builds – Trifold Brochure</title>
<link rel="stylesheet" href="https://fonts.googleapis.com/css2?family=Montserrat:wght@400;500;600;700&display=swap">
<style>
  :root{
    --navy:#1d2a40;
    --slate:#36465f;
    --steel:#5b6b82;
    --paper:#ffffff;
    --mist:#eceef1;
    --fog:#d9dce1;
    --ink:#1b2233;
    --body:#2c3344;
    --gold:#b89a5e;
    --stage:#e4e5e7;
  }
  *{box-sizing:border-box;margin:0;padding:0}
  html,body{width:1200px;height:900px;overflow:hidden}
  body{background:var(--stage);font-family:"Montserrat",Arial,sans-serif;color:var(--body);position:relative}
  .spread{position:absolute;left:150px;width:900px;height:420px;display:flex;box-shadow:0 6px 18px rgba(0,0,0,.12)}
  .spread--outside{top:22px}
  .spread--inside{top:460px}
  .panel{position:relative;width:300px;height:420px;overflow:hidden;background:var(--paper)}
  .panel + .panel{border-left:1px solid rgba(0,0,0,.06)}
  .heading{font-weight:600;color:var(--ink);text-transform:uppercase;letter-spacing:.2px;line-height:1}
  .heading--xl{font-size:22px}
  .heading--lg{font-size:17px}
  .subheading{font-size:12px;font-weight:600;color:var(--ink);text-transform:uppercase;margin-top:2px}
  .rule{width:130px;height:2px;background:var(--navy);margin:4px 0 8px}
  .copy{font-size:7.6px;line-height:1.38;color:var(--body)}
  .copy + .copy{margin-top:6px}
  .photo{position:absolute;display:block}
  .band{position:absolute;left:0;width:100%}

  /* outside */
  .about{padding:26px 24px 0}
  .about .copy{width:200px}
  .contact__cta{position:absolute;top:160px;left:0;width:100%;text-align:center}
  .contact__cta strong{display:block;font-size:19px;font-weight:700;color:var(--ink);letter-spacing:.8px}
  .contact__cta span{display:block;font-size:13px;font-weight:500;color:var(--ink);margin-top:2px}
  .contact__list{position:absolute;top:222px;left:24px;list-style:none}
  .contact__list li{display:flex;align-items:flex-start;gap:9px;font-size:8.3px;font-weight:600;color:var(--ink);margin-bottom:12px;line-height:1.35}
  .contact__list svg{flex:none;width:11px;height:11px}
  .cover{background:linear-gradient(180deg,#5a6274 0%,#2f3a52 45%,#1b2740 100%);color:#fff}
  .cover__title{position:absolute;top:52px;left:20px;text-transform:uppercase;font-weight:600;line-height:1.1}
  .cover__title b{display:block;font-size:20px;font-weight:600;letter-spacing:.6px}
  .cover__title span{display:block;font-size:13px;letter-spacing:.5px}
  .brand{position:absolute;top:220px;left:20px;display:flex;align-items:center;gap:8px}
  .brand__mark{width:22px;height:22px;background:var(--gold)}
  .brand__name{font-size:15px;font-weight:500;letter-spacing:2px;color:#fff;text-transform:uppercase}
  .cover__tagline{position:absolute;top:270px;left:20px;font-size:7.4px;line-height:1.75;letter-spacing:.4px;text-transform:uppercase;color:#e6e9ef}

  /* inside */
  .why{background:linear-gradient(180deg,#dcdfe3 0%,#eef0f2 60%,#e2e4e8 100%);padding:26px 22px 0}
  .services{background:var(--paper);padding:26px 18px 0}
  .services .heading--lg{margin-top:12px}
  .housing{background:var(--paper);padding:26px 20px 0}
  .housing .heading--lg{margin-top:8px;margin-bottom:6px}
  .why .copy,.services .copy,.housing .copy{font-size:7.3px}
  .why .heading--xl{margin-bottom:8px}
  .services .heading--xl{font-size:20px}
</style>
</head>
<body>

<section class="spread spread--outside" aria-label="Brochure outside">
  <article class="panel about">
    <h2 class="heading heading--xl">About us</h2>
    <div class="rule"></div>
    <p class="copy">With a wealth of experience in all construction methods from steel and RC frame apartment blocks to timber frame and traditional masonry housing, we take pride in our ability to take on the most challenging and architecturally spectacular projects. No job is too big or too complex for our team of professionals.</p>
    <div class="photo" role="img" aria-label="Photograph of a modern white detached house with solar panels on the roof" style="left:0;top:232px;width:300px;height:165px;background:linear-gradient(160deg,#9fb0c6 0%,#c9cdd2 45%,#8e8a80 100%)"></div>
    <svg class="band" style="top:240px;height:180px" viewBox="0 0 300 180" preserveAspectRatio="none" aria-hidden="true">
      <polygon points="0,0 300,0 300,22 0,40" fill="var(--paper)"/>
      <rect x="0" y="158" width="300" height="22" fill="var(--slate)"/>
    </svg>
  </article>

  <article class="panel contact">
    <div class="photo" role="img" aria-label="Photograph of a luxury open-plan interior with large glazed doors" style="left:0;top:0;width:300px;height:140px;background:linear-gradient(135deg,#3a3f4a 0%,#6f6a62 45%,#2b3040 100%)"></div>
    <svg class="band" style="top:100px;height:50px" viewBox="0 0 300 50" preserveAspectRatio="none" aria-hidden="true">
      <polygon points="0,50 300,50 300,0 0,40" fill="var(--paper)"/>
    </svg>
    <div class="contact__cta"><strong>Contact us</strong><span>today to learn more</span></div>
    <ul class="contact__list">
      <li><svg viewBox="0 0 12 12"><circle cx="6" cy="6" r="6" fill="var(--ink)"/><path d="M4 3.2l1 1.3-.6.7c.4.9 1 1.5 1.9 1.9l.7-.6 1.3 1-.5 1c-2.4-.2-4.3-2.1-4.5-4.5z" fill="#fff"/></svg>0203 555 0142</li>
      <li><svg viewBox="0 0 12 12"><circle cx="6" cy="6" r="6" fill="var(--ink)"/><circle cx="6" cy="6" r="3.3" fill="none" stroke="#fff" stroke-width=".8"/><path d="M2.7 6h6.6M6 2.7c-1.4 1.8-1.4 4.8 0 6.6M6 2.7c1.4 1.8 1.4 4.8 0 6.6" fill="none" stroke="#fff" stroke-width=".7"/></svg>info@holvane-builds.co.uk</li>
      <li><svg viewBox="0 0 12 12"><circle cx="6" cy="6" r="6" fill="var(--ink)"/><path d="M6 2.6a2.3 2.3 0 0 1 2.3 2.3C8.3 6.6 6 9.4 6 9.4S3.7 6.6 3.7 4.9A2.3 2.3 0 0 1 6 2.6z" fill="#fff"/><circle cx="6" cy="4.9" r=".9" fill="var(--ink)"/></svg>Office 12,<br>40 Larkfield Road,<br>Ashbury,<br>AB1 2CD</li>
    </ul>
    <svg class="band" style="bottom:0;height:22px" viewBox="0 0 300 22" preserveAspectRatio="none" aria-hidden="true">
      <rect width="300" height="22" fill="var(--slate)"/>
    </svg>
  </article>

  <article class="panel cover">
    <div class="photo" role="img" aria-label="Photograph of a contemporary home terrace with a pool at dusk" style="left:0;top:0;width:300px;height:190px;background:linear-gradient(180deg,#7d8597 0%,#5c6576 60%,#3a4a66 100%);opacity:.9"></div>
    <svg class="band" style="top:150px;height:60px" viewBox="0 0 300 60" preserveAspectRatio="none" aria-hidden="true">
      <polygon points="0,60 300,60 300,10 0,40" fill="#1f2b44" opacity=".9"/>
    </svg>
    <h1 class="cover__title"><b>A wealth</b><span>of experience</span></h1>
    <div class="brand"><span class="brand__mark"></span><span class="brand__name">Holvane Builds</span></div>
    <p class="cover__tagline">Specialize in building<br>very high specification,<br>luxury houses<br>and large volume<br>residential developments.</p>
  </article>
</section>

<section class="spread spread--inside" aria-label="Brochure inside">
  <article class="panel why">
    <h2 class="heading heading--xl">Why<br>choose us</h2>
    <p class="copy">With a wealth of experience in all construction methods from steel and RC frame apartment blocks to timber frame and traditional masonry housing, we take pride in our ability to take on the most challenging and architecturally spectacular projects. No job is too big or too complex for our team of professionals. When searching for a construction company to complete your project, you must out your trust in the hands of true professionals to work on your property.</p>
    <p class="copy">At Holvane Builds, we specialize in building very high specification, luxury houses and large volume residential developments for the wider housing market. We have built single luxury houses up to a build value of £8 million and have managed multiple unit housing developments up to a value of £52 million.</p>
    <svg class="band" style="bottom:0;height:60px" viewBox="0 0 300 60" preserveAspectRatio="none" aria-hidden="true">
      <polygon points="0,40 300,60 0,60" fill="var(--slate)"/>
    </svg>
  </article>

  <article class="panel services">
    <svg class="band" style="top:0;left:auto;right:-300px;height:22px" viewBox="0 0 300 22" preserveAspectRatio="none" aria-hidden="true"></svg>
    <h2 class="heading heading--xl">Our<br>services</h2>
    <p class="subheading">The build specialists</p>
    <p class="copy" style="margin-top:8px">At Holvane Builds we are passionate about helping you build your perfect home. We offer a wide range of practical solutions to suit all your residential construction needs. Whether your project is a large housing development, blocks of apartments or a one off bespoke luxury house, we have the experience and the know how to deliver a project that exceeds your requirements.</p>
    <h3 class="heading heading--lg">Luxury homes</h3>
    <p class="copy" style="margin-top:8px">At Holvane Builds we are very fortunate to be specialists at working on very high end luxurious residential properties. We work closely with our clients and their design team to build dream homes that are unique, luxurious and architecturally splendid. Architects and designers will always appreciate the practical input of a construction team that can offer</p>
    <svg class="band" style="bottom:0;height:22px" viewBox="0 0 300 22" preserveAspectRatio="none" aria-hidden="true">
      <rect width="300" height="22" fill="var(--slate)"/>
    </svg>
  </article>

  <article class="panel housing">
    <svg class="band" style="top:0;height:26px" viewBox="0 0 300 26" preserveAspectRatio="none" aria-hidden="true">
      <polygon points="0,0 40,0 0,12" fill="var(--navy)"/>
    </svg>
    <p class="copy">solutions which allow the design concept to be brought to life without compromise.<br>We adore fine finishes and bespoke design features that make each one of our luxury homes unique and a dream come true for the homeowner. Through a combination of insisting on only using the best tradesmen for the job and tight quality controls we ensure an immaculate finish that will impress all who employ our services or visit one of our finished homes.</p>
    <h3 class="heading heading--lg">Housing<br>developments</h3>
    <p class="copy">At Holvane Builds we don’t just specialise in very high-end residential projects, we also have decades of experience building volume residential housing developments consisting of multiple houses or blocks of apartments.</p>
    <p class="copy" style="margin-top:10px">Utilising our NQAB approved building management systems we have developed we can provide excellent quality control, health and safety and value for housing developers who require the experience and expertise that only a few construction companies can provide.</p>
    <svg class="band" style="bottom:0;height:60px" viewBox="0 0 300 60" preserveAspectRatio="none" aria-hidden="true">
      <polygon points="0,60 300,38 300,60" fill="var(--slate)"/>
    </svg>
  </article>
</section>

<svg style="position:absolute;left:450px;top:460px;width:150px;height:14px" viewBox="0 0 150 14" preserveAspectRatio="none" aria-hidden="true">
  <polygon points="0,0 150,0 150,14" fill="var(--navy)"/>
</svg>

</body>
</html>
```